Brisk Meadow Builders needs a product brochure

We need a new flyer for our Patio Perch Lounge. Here is some of the copy your will need.
"Turn your back yard into the ultimate entertianment venue with the stunning Patio Perch Lounge!"
"Entertain family & friends in your very own back yard!"
"Available with or without solar and comes in a variety of colors"
"The Patio Perch Lounge measures 5' deep by 10' wide and is 9'-6" at it's highest point"
"Constructed with treated 4x4's, primed then painted with Thornby Calder best exterior paint for years of care free enjoyment. Also, Marlow Pendt Keystead shingles are dimensional, have a 25 year warranty and are rated for 150 mph winds!"
"TV Mount included. Shelves and TV are sold separately"
There also needs to be a box where we can add the price into later. The price can change from time to time due to material cost fluctuation.
Look and feel
Each slider illustrates characteristics of the customer's brand and the style your logo design should communicate.

```html
<!DOCTYPE html>
<html lang="en">
<head>
<meta charset="utf-8">
<title>Patio Perch Lounge Flyer</title>
<link href="https://fonts.googleapis.com/css2?family=Barlow:wght@400;500;600;700;800;900&family=Barlow+Condensed:wght@600;700&display=swap" rel="stylesheet">
<style>
  :root {
    --green: #3a8a3f;
    --green-dark: #2a6e32;
    --orange: #f7ab1b;
    --ink: #1e1e1e;
    --panel: #f3f3f4;
    --white: #ffffff;
  }
  * { box-sizing: border-box; margin: 0; padding: 0; }
  html, body { width: 735px; height: 1200px; overflow: hidden; background: var(--white); }
  .flyer { position: relative; width: 735px; height: 1200px; font-family: "Barlow", sans-serif; color: var(--ink); overflow: hidden; }
  .backdrop { position: absolute; inset: 0; }

  .brand { position: absolute; left: 34px; top: 64px; display: flex; align-items: center; gap: 8px; }
  .brand-dot { width: 14px; height: 14px; border-radius: 50%; background: var(--green); }
  .brand-name { font-weight: 700; font-size: 19px; color: var(--orange); letter-spacing: 0.3px; }

  .headline { position: absolute; left: 46px; top: 540px; color: var(--white); font-family: "Barlow Condensed", sans-serif; font-weight: 700; font-size: 37px; line-height: 34px; }
  .headline .accent { color: var(--orange); margin-left: 8px; }

  .thumb { position: absolute; top: 645px; width: 176px; height: 166px; border-radius: 22px; border: 4px solid var(--green-dark); }
  .thumb-opener { left: 20px; background: linear-gradient(135deg, #8fa37e, #b9b0a2 50%, #8b5a3c); }
  .thumb-rack { left: 210px; background: linear-gradient(180deg, #3b3b3b 0%, #5a4634 40%, #b8733a 100%); }

  .features { position: absolute; left: 19px; top: 823px; width: 392px; height: 308px; background: var(--panel); border-radius: 18px; padding: 20px 14px 0 14px; list-style: none; font-size: 14.5px; line-height: 21px; }
  .features li { position: relative; padding-left: 22px; margin-bottom: 11px; }
  .features li::before { content: ""; position: absolute; left: 0; top: 7px; width: 8px; height: 8px; border-radius: 50%; background: var(--ink); }

  .badge-text { position: absolute; left: 395px; top: 520px; width: 340px; text-align: center; color: var(--white); }
  .badge-lead { font-family: "Barlow Condensed", sans-serif; font-weight: 700; font-size: 24px; line-height: 26px; }
  .badge-title { margin-top: 8px; font-weight: 900; font-size: 37px; line-height: 40px; color: var(--orange); letter-spacing: 0.5px; }

  .tagline { position: absolute; left: 440px; top: 818px; width: 270px; text-align: center; font-size: 23px; line-height: 29px; font-weight: 500; }
  .tagline strong { color: var(--green-dark); font-weight: 700; }

  .price-box { position: absolute; left: 474px; top: 925px; width: 200px; height: 185px; border-radius: 14px; background: linear-gradient(135deg, var(--green-dark), var(--green) 60%, #2f7a37); color: var(--white); text-align: center; padding-top: 16px; font-size: 28px; line-height: 29px; font-weight: 500; }

  .contact-bar { position: absolute; left: 0; bottom: 0; width: 735px; height: 51px; background: var(--orange); display: flex; align-items: center; justify-content: center; gap: 30px; color: var(--white); font-size: 17px; }
  .contact-item { display: flex; align-items: center; gap: 9px; }
  .contact-icon { width: 16px; height: 16px; }
</style>
</head>
<body>
<main class="flyer">
  <svg class="backdrop" viewBox="0 0 735 1200" width="735" height="1200" aria-hidden="false">
    <defs>
      <linearGradient id="photoTone" x1="0" y1="0" x2="1" y2="1">
        <stop offset="0" stop-color="#9cb27a"/>
        <stop offset="0.35" stop-color="#7d7f80"/>
        <stop offset="0.65" stop-color="#5e4a38"/>
        <stop offset="1" stop-color="#8d8f92"/>
      </linearGradient>
      <linearGradient id="greenBand" x1="0" y1="0" x2="1" y2="0">
        <stop offset="0" stop-color="#2a6e32"/>
        <stop offset="1" stop-color="#3d9142"/>
      </linearGradient>
    </defs>
    <!-- orange swoosh behind the hero photo -->
    <path d="M0 250 L495 0 H735 V600 H0 Z" fill="var(--orange)"/>
    <!-- hero photo -->
    <path role="img" aria-label="Photo of the Patio Perch Lounge outdoor bar with solar panel roof, mounted TV, shelves, bar stools and a cooler on a paved patio" d="M80 212 L458 0 H735 V440 Q600 530 430 548 Q250 535 80 470 Z" fill="url(#photoTone)"/>
    <!-- green band under headline -->
    <path d="M0 445 Q200 525 440 560 V629 H0 Z" fill="url(#greenBand)"/>
    <!-- green corner wedge on the right -->
    <path d="M735 430 V560 H620 Q690 510 735 430 Z" fill="var(--green-dark)"/>
    <!-- white ring and badge ellipse -->
    <ellipse cx="570" cy="635" rx="188" ry="154" fill="var(--white)"/>
    <ellipse cx="570" cy="635" rx="180" ry="146" fill="url(#greenBand)"/>
    <!-- orange accents -->
    <path d="M0 810 Q22 880 0 960 Z" fill="var(--orange)"/>
    <path d="M0 960 Q12 1010 0 1050 Z" fill="var(--orange)"/>
    <path d="M411 1022 Q440 1028 467 1022 V1096 Q440 1086 411 1096 Z" fill="var(--orange)"/>
    <path d="M682 992 Q715 968 735 940 L735 948 Q718 975 686 998 Z" fill="var(--orange)"/>
    <path d="M640 560 Q700 520 735 470 L735 478 Q705 528 646 566 Z" fill="var(--white)"/>
  </svg>

  <div class="brand">
    <span class="brand-dot"></span>
    <span class="brand-name">Brisk Meadow Builders</span>
  </div>

  <h1 class="headline">TURN<br>YOUR<span class="accent">BACK YARD INTO</span></h1>

  <div class="thumb thumb-opener" role="img" aria-label="Photo of a hand opening a bottle on the bar's mounted opener next to a football"></div>
  <div class="thumb thumb-rack" role="img" aria-label="Photo of a wall shelf holding wine bottles with hanging wine glasses below"></div>

  <ul class="features">
    <li>Available with or without solar and comes in a variety of colors</li>
    <li>The Patio Perch Lounge measures 5' deep by 10' wide and is 9'-6" at it's highest point</li>
    <li>TV Mount included. Shelves and TV are sold separately</li>
    <li>Constructed with treated 4x4's, primed then painted with Thornby Calder best exterior paint for years of care free enjoyment. Also, Marlow Pendt Keystead shingles are dimensional, have a 25 year warranty and are rated for 150 mph winds!</li>
  </ul>

  <div class="badge-text">
    <p class="badge-lead">THE ULTIMATE<br>ENTERTIANMENT VENUE<br>WITH</p>
    <p class="badge-title">THE STUNNING<br>PATIO PERCH<br>LOUNGE!</p>
  </div>

  <p class="tagline">Entertain family &amp; friends<br>in your<br><strong>very own back yard!</strong></p>

  <div class="price-box">STARTING<br>AT JUST</div>

  <footer class="contact-bar">
    <span class="contact-item">
      <svg class="contact-icon" viewBox="0 0 16 16"><circle cx="8" cy="8" r="8" fill="#fff"/><rect x="4" y="5" width="8" height="6" rx="1" fill="var(--orange)"/><path d="M4.5 5.5 L8 8.5 L11.5 5.5" stroke="#fff" stroke-width="1" fill="none"/></svg>
      info@briskmeadow.com
    </span>
    <span class="contact-item">
      <svg class="contact-icon" viewBox="0 0 16 16"><circle cx="8" cy="8" r="8" fill="#fff"/><circle cx="8" cy="8" r="4.5" fill="none" stroke="var(--orange)" stroke-width="1.2"/><path d="M3.5 8 H12.5 M8 3.5 V12.5" stroke="var(--orange)" stroke-width="1"/></svg>
      www.briskmeadow.com
    </span>
    <span class="contact-item">
      <svg class="contact-icon" viewBox="0 0 16 16"><circle cx="8" cy="8" r="8" fill="#fff"/><path d="M5.5 4 L7 4.3 L7.4 6.3 L6.5 7 Q7.3 8.8 9 9.5 L9.7 8.6 L11.7 9 L12 10.5 Q11.5 12 10 12 Q5 11.5 4 6 Q4 4.5 5.5 4 Z" fill="var(--orange)"/></svg>
      555-014-0192
    </span>
  </footer>
</main>
</body>
</html>
```